Business Card Design Project

Attached is a rough business card design. We like this general design but we feel that the layout, text, color can use improvement and we seek the help of a professional designer.
We have a television and film production company based in New York. We need our cards for television network executives, other production executives, financiers etc. We deal with creative types as well as business people so we need the card to be interesting and edgy just like the name of our company - KICKTHEDOOR. The design should reflect the edgy, punk rock attitude of our company.
We prefer orange typeface for the logo but we're open to other ideas. I am attaching our existing business card and other files to help with the design.
Thank you in advance!!
Updates
Target Market(s)
Television and film producers, television network executives, other production executives, financiers, distribution companies
Industry/Entity Type
Film Production
Requirements
Must have
- I am attaching a photo of the company mascot which is a dog. We prefer to have the dog's photo as part of the card but we're open to the other ideas.
Name, phone number, email

```html
<!DOCTYPE html>
<html lang="en">
<head>
<meta charset="utf-8">
<title>KICKTHEDOOR – Business Card</title>
<link rel="stylesheet" href="https://fonts.googleapis.com/css2?family=Mulish:wght@300;700&display=swap">
<style>
  :root {
    --page: #ffffff;
    --card-edge: #d6d6d6;
    --brand-orange: #fc3a0c;
    --ink: #111111;
    --paper: #ffffff;
    --photo-light: #f3e4ea;
    --photo-mid: #d9a58c;
    --photo-dark: #7a4a3c;
  }
  html, body {
    margin: 0;
    width: 1200px;
    height: 1000px;
    overflow: hidden;
    background: var(--page);
  }
  .canvas {
    position: relative;
    width: 1200px;
    height: 1000px;
  }
  .business-card {
    position: absolute;
    left: 98px;
    top: 175px;
    width: 1004px;
    height: 650px;
    box-shadow: 0 0 0 1px var(--card-edge), 0 1px 3px rgba(0,0,0,0.08);
  }
  .business-card svg { display: block; }
  .wordmark {
    font-family: "Mulish", sans-serif;
    font-weight: 300;
    font-size: 76px;
    letter-spacing: 4px;
    fill: var(--ink);
  }
  .contact-name {
    font-family: "Mulish", sans-serif;
    font-weight: 700;
    font-size: 25px;
    fill: var(--paper);
  }
  .contact-line {
    font-family: "Mulish", sans-serif;
    font-weight: 300;
    font-size: 25px;
    fill: var(--paper);
  }
  .icon-tile { fill: var(--paper); }
  .icon-glyph { fill: none; stroke: var(--brand-orange); stroke-width: 3; stroke-linejoin: round; stroke-linecap: round; }
</style>
</head>
<body>
<div class="canvas">
  <div class="business-card">
    <svg width="1004" height="650" viewBox="0 0 1004 650" xmlns="http://www.w3.org/2000/svg">
      <defs>
        <linearGradient id="mascot-tones" x1="0" y1="0" x2="1" y2="1">
          <stop offset="0" stop-color="var(--photo-light)"/>
          <stop offset="0.35" stop-color="var(--photo-mid)"/>
          <stop offset="0.65" stop-color="var(--photo-dark)"/>
          <stop offset="1" stop-color="var(--photo-light)"/>
        </linearGradient>
      </defs>

      <rect class="mascot-photo" x="0" y="0" width="560" height="650" fill="url(#mascot-tones)"
            role="img" aria-label="Photo of the company mascot, a fawn French bulldog resting its head on the floor"/>

      <polygon class="brand-panel" points="267,0 1004,0 1004,650 517,650" fill="var(--brand-orange)"/>

      <text class="wordmark" transform="translate(412,292) rotate(-21)">kickthedoor</text>

      <text class="contact-name" transform="translate(446,362) rotate(-20)">Marcus Delgado</text>

      <g class="contact-phone" transform="translate(462,372) rotate(-20)">
        <rect class="icon-tile" x="0" y="0" width="36" height="36"/>
        <path class="icon-glyph" d="M11 8 l5 0 l2 6 l-3 2 q3 6 8 8 l2 -3 l6 2 l0 5 q-14 1 -20 -20 z"/>
        <text class="contact-line" x="46" y="28">917-555-0182</text>
      </g>

      <g class="contact-email" transform="translate(480,420) rotate(-20)">
        <rect class="icon-tile" x="0" y="0" width="36" height="36"/>
        <rect class="icon-glyph" x="6" y="10" width="24" height="17"/>
        <path class="icon-glyph" d="M6 10 l12 10 l12 -10"/>
        <text class="contact-line" x="46" y="28">Marcus@kickthedoor.com</text>
      </g>
    </svg>
  </div>
</div>
</body>
</html>
```